Launching a business called "QTNB", a foreign exchange “Clearing House”.

We need urgently:
- business logo
- Wordpress 4.5.2 responsive homepage + template
- headed paper templates for LibreOffice + Google Docs
- business cards
- e-Mail signature

Note: only design, will do the html integration ourselves.

Brief & guidelines:
Our target audience are financial institutions (medium to very large), some very savvy, some more conservative. Corporate image needs to be clean and trustworthy, yet the business is a disruptor concept based on "blockchain" technology that comes from the Plenthium world.
The difficulty is to mix the Fintech attraction of cryptocurrencies and blockchain with the seriousness of investment banking finance.

=> Big no-no: cannot look like a retail foreign exchange business offering! QTNB is strictly an institutional service, no cute banknote design or graphics suggesting travel service etc.

QTNB image should =
50% Technology "Fintech"
20% Financial markets utility
15% Foreign Exchange
10% Settlement security
5% Investment Banking service

Explanations:
* Technology "Fintech" -> QTNB is a startup, and fits the "Fintech" profile. The Clearing House uses new technology (Blockchain) to settle FX transactions between participants.
* Financial markets utility -> A "Clearing house" is a central counterparty that helps effect all payments between participants by being the central hub for all transactions.
* Foreign Exchange -> Our service is exclusively focused on Spot Foreign Exchange
* Settlement security -> The role of the clearing house is to guarantee that everyone gets paid. It collects security deposits from participants to protect all sides from anyone's default. A good clearing house is rock solid and trusted by everyone.
* Investment Banking service -> QTNB only offers its service to institutions. Accredited investors only !

business logo
Letter based logo (QTNB obviously) and optionally full words "QT Netting Bureau" as well. Don't worry about being BORING, this is not Limber-Pop and we don't need to appeal to the general public. Need to be easily recognised though...

Wordpress 4.5.2 compatible responsive homepage + template
Our web engineer uses that Wordpress version. The homepage is a "long scroll" with most info in sections as most startups in Silicon valley. Additional pages (template) added and accessible via the navigation menu.

Headed paper LibreOffice + Google Docs
Consistent branding templates for text editors LibreOffice and Google Docs.

Business cards
Either single or 2 sided, bit more freedom for the design. We need space for ->
Phone: mobile: e-Mail: Skype: Address: SIP: Slack: Google:
Could include a QR code on the back side for the tech savvy (example file attached).

e-Mail signature
HTML signature that we will use with Thunderbird, containing details of the business card plus possibly a short legal disclaimer.

Example web sites and why we like them:
https://www.brellwick.example/features/networking/
Clean, white spaces, not too much text (no one reads much these days), graphics do the explaining.
https://www.pontivo.example/
The best (apart from the childish graphics). Long scroll, graphics that explain, colour delimited sections, links to more resources, simple top navigation.
https://sarnfold.example/how-it-works/
Clean and simple header, tech graphics. Don't like full width text and no sections.
http://www.vqm.example/home
Only Financial site we don't dislike too much. It is clean and simple, not too cramped and feels friendly. Not very high-tech though...

Some Blockchain related sites and mix graphics, no particular likes, but just to give ideas on how others have captured the tech image of Blockchain/Distributed-ledger:
http://shortlk.example/7h3kQpZ
http://shortlk.example/4mRw8Tn
http://shortlk.example/9cYvD2s
http://shortlk.example/3bNx5Jh
=> Careful not to fall into "The Orchard" trap. Technology mastery, not MYSTERY. The presence of numbers could allow to put recognisable FX prices if need be. We don’t like dark/black backgrounds in general...

Our target audience are financial institutions (medium to very large), some very savvy, some more conservative.

Financial Service

Either single or 2 sided, bit more freedom for the design than the Website. We need space for ->

QTNB (optionally can add "The QT Netting bureau")

2 page

Sans Serif

• Wordpress 4.5.2 compatible responsive homepage
• Our web engineer uses that Wordpress version. The homepage is a "long scroll" with most info in sections as most startups in Silicon valley.
• Additional pages: accessible via the navigation menu, based on 1 template that we would like you to design.
• Cannot look like a retail (private investor) foreign exchange business offering! QTNB is strictly an institutional service, no cute banknote designs or graphics suggesting travel service etc.

```html
<!DOCTYPE html>
<html lang="en">
<head>
<meta charset="utf-8">
<title>QT Netting Bureau — Home</title>
<link rel="stylesheet" href="https://fonts.googleapis.com/css2?family=Jost:wght@300;400;500&display=swap">
<style>
:root{
  --navy:#0d1b3a;
  --navy-deep:#0a1430;
  --yellow:#f6e31c;
  --gold:#b3961a;
  --teal-text:#1d6c8c;
  --muted:#a9adb6;
  --white:#ffffff;
  --ink:#1a1a1a;
  --slate:#4f5966;
}
*{box-sizing:border-box;margin:0;padding:0}
html,body{width:1200px;height:2575px;overflow:hidden}
body{position:relative;background:var(--navy-deep);font-family:'Jost',sans-serif;color:var(--ink)}
.abs{position:absolute}

/* header */
.site-header{left:0;top:0;width:1200px;height:151px;background:var(--white)}
.call-us{right:6px;top:0;width:240px;height:34px;background:var(--navy);color:var(--white);font-size:13px;display:flex;align-items:center;justify-content:center;gap:8px;letter-spacing:.3px}
.brand{left:50px;top:58px;display:flex;align-items:center;gap:12px;font-size:32px;font-weight:500;color:var(--navy)}
.brand-mark{width:18px;height:18px;background:var(--navy)}
.main-nav{left:472px;top:66px;display:flex;gap:32px;font-size:18px;color:var(--ink);align-items:center}
.signup{right:48px;top:62px;width:100px;height:34px;border-radius:17px;background:var(--yellow);font-size:15px;display:flex;align-items:center;justify-content:center}

/* hero */
.hero{left:0;top:151px;width:1200px;height:505px;background:linear-gradient(180deg,#2b3447 0%,#3a3e4a 45%,#23293a 100%)}
.hero-title{left:50px;top:330px;font-size:51px;font-weight:400;line-height:56px;color:var(--white);letter-spacing:.5px}
.hero-lead{left:50px;top:450px;width:800px;font-size:19px;line-height:24px;color:#e4e6ea;font-weight:300}
.hero-cta{left:50px;top:521px;width:192px;height:44px;border-radius:22px;background:var(--white);font-size:17px;font-weight:500;display:flex;align-items:center;justify-content:center;color:var(--navy)}
.hero-device{left:886px;top:283px;width:292px;height:426px;border-radius:18px;background:linear-gradient(160deg,#3c1a6b,#23103f)}

/* shared section heading */
.section-title{left:0;width:1200px;text-align:center;font-size:27px;line-height:31px;font-weight:400}
.rule{left:557px;width:86px;height:5px;background:var(--navy)}
.section-sub{left:0;width:1200px;text-align:center;font-size:16px;color:var(--muted);font-weight:300}

/* features */
.features{left:0;top:656px;width:1180px;height:456px;background:var(--white)}
.features .section-title{width:1200px;color:var(--navy)}
.hex{width:123px;height:141px}
.feature-label{left:283px;top:1028px;width:137px;text-align:center;color:var(--yellow);font-size:19px;line-height:23px;font-weight:500}
.feature-arrow{left:440px;top:1040px}
.feature-text{left:466px;top:1027px;width:460px;font-size:15.5px;line-height:20px;color:var(--muted);font-weight:300}

/* dashboard band */
.dashboard{left:0;top:1128px;width:1200px;height:470px;background:linear-gradient(90deg,#2a1746 0%,#263a63 50%,#227086 100%);border:10px solid var(--navy-deep)}
.dashboard-title{color:var(--white)}
.dashboard-title .hl{color:var(--yellow)}
.dashboard .rule{background:var(--navy-deep)}
.dashboard-sub{color:#e2e6ee}
.hands-tablet{left:240px;top:1320px;width:430px;height:272px;border-radius:14px 14px 0 0;background:linear-gradient(180deg,#1d1d22,#6b5a52)}
.dashboard-text{left:648px;top:1334px;width:272px;font-size:17px;line-height:21px;color:var(--white);font-weight:300}
.btn{height:40px;border-radius:20px;font-size:16px;font-weight:500;display:flex;align-items:center;justify-content:center;box-shadow:2px 3px 0 rgba(0,0,0,.35)}
.btn-yellow{background:var(--yellow);color:var(--navy)}
.btn-slate{background:var(--slate);color:var(--white)}

/* security */
.security{left:21px;top:1617px;width:1159px;height:435px;background:var(--white)}
.security-title{color:var(--navy)}
.security-title .hl{color:var(--teal-text)}
.security-heading{left:312px;top:1814px;width:408px;padding-bottom:8px;border-bottom:1px solid #ddd;font-size:21px;color:var(--gold);letter-spacing:.5px}
.security-text{left:309px;top:1860px;width:410px;font-size:16.5px;line-height:20px;color:var(--ink);text-align:justify}
.padlock{left:763px;top:1802px;width:197px;height:223px;border-radius:40px 40px 10px 10px;background:linear-gradient(180deg,#b9bcc2 0%,#3c4a63 45%,#1f2a40 100%)}

/* locations */
.locations{left:21px;top:2077px;width:1159px;height:478px;background:linear-gradient(160deg,#ecebe6 0%,#e3e1d8 60%,#efe6c8 100%)}
.locations-title{color:var(--navy)}
.locations-title .hl{color:var(--gold)}
.envelope{left:318px;top:2275px;width:248px;height:197px;border-radius:6px;background:linear-gradient(180deg,#e9ecef 0%,#e3503f 45%,#c23a2c 100%)}
.contact{left:577px;top:2282px;font-size:17px;line-height:26.6px;color:var(--ink)}
.contact-col2{left:771px}
.tag{display:inline-block;background:var(--navy);color:var(--white);padding:0 6px;line-height:21px;width:151px}
.contact .browse{color:var(--yellow)}
.row{height:26.6px}
</style>
</head>
<body>

<header class="abs site-header">
  <div class="abs call-us">
    <svg width="18" height="18" viewBox="0 0 18 18"><circle cx="9" cy="9" r="8" fill="none" stroke="#fff" stroke-width="1.4"/><path d="M6 5l2 2-1 1c.5 1.2 1.3 2 2.5 2.5l1-1 2 2-1.2 1.2C8.5 12.5 5.5 9.5 4.8 6.2z" fill="#fff"/></svg>
    CALL US 555-014-7788
  </div>
  <div class="abs brand"><span class="brand-mark"></span>QT Netting Bureau</div>
  <nav class="abs main-nav">
    <span>Products</span><span>How It Works</span><span>Gallery</span><span>Qualifications</span><span>Features</span>
  </nav>
  <div class="abs signup">Signup</div>
</header>

<section class="abs hero" role="img" aria-label="Night photograph of a dense city skyline of office towers"></section>
<h1 class="abs hero-title">LOREM IPSUM DOLOR SIT AMET,<br>CONSECTETUER ADIPISCING</h1>
<p class="abs hero-lead">Lorem ipsum dolor sit amet, consectetuer adipiscing elit, sed diam nonummy nibh euismod tincidunt ut laoreet dolore magna aliquam erat volutpat.</p>
<div class="abs hero-cta">GET STARTED</div>
<div class="abs hero-device" role="img" aria-label="Illustration of a tablet showing a connected network of nodes"></div>

<section class="abs features"></section>
<h2 class="abs section-title" style="top:717px;color:var(--navy)">High Profile Support For Distributed<br>Blockchain Technology</h2>
<div class="abs rule" style="top:792px"></div>
<p class="abs section-sub" style="top:810px">Lorem ipsum dolor sit amet, consectetuer adipiscing elit.</p>

<svg class="abs hex" style="left:288px;top:867px" viewBox="0 0 123 141"><polygon points="61.5,0 123,35 123,106 61.5,141 0,106 0,35" fill="#0d1b3a"/><circle cx="61.5" cy="66" r="18" fill="#f6e31c"/><rect x="53" y="86" width="17" height="10" rx="2" fill="#f6e31c"/><text x="61.5" y="74" text-anchor="middle" font-family="Jost,sans-serif" font-size="22" font-weight="500" fill="#0d1b3a">$</text><g stroke="#f6e31c" stroke-width="3"><line x1="61.5" y1="30" x2="61.5" y2="40"/><line x1="34" y1="45" x2="41" y2="50"/><line x1="89" y1="45" x2="82" y2="50"/><line x1="28" y1="66" x2="37" y2="66"/><line x1="95" y1="66" x2="86" y2="66"/></g></svg>
<svg class="abs hex" style="left:453px;top:867px" viewBox="0 0 123 141"><polygon points="61.5,0 123,35 123,106 61.5,141 0,106 0,35" fill="#0d1b3a"/><rect x="34" y="52" width="55" height="37" rx="4" fill="none" stroke="#aeb9c7" stroke-width="4"/><rect x="41" y="58" width="41" height="25" rx="2" fill="#aeb9c7"/><circle cx="61.5" cy="70.5" r="8" fill="#0d1b3a"/></svg>
<svg class="abs hex" style="left:619px;top:867px" viewBox="0 0 123 141"><polygon points="61.5,0 123,35 123,106 61.5,141 0,106 0,35" fill="#0d1b3a"/><path d="M48 62v-8a13.5 13.5 0 0 1 27 0v8" fill="none" stroke="#aeb9c7" stroke-width="4"/><rect x="42" y="62" width="39" height="31" rx="4" fill="none" stroke="#aeb9c7" stroke-width="4"/><circle cx="61.5" cy="75" r="4" fill="#aeb9c7"/><rect x="59.5" y="76" width="4" height="9" fill="#aeb9c7"/></svg>
<svg class="abs hex" style="left:784px;top:867px" viewBox="0 0 123 141"><polygon points="61.5,0 123,35 123,106 61.5,141 0,106 0,35" fill="#0d1b3a"/><rect x="33" y="52" width="57" height="38" rx="6" fill="none" stroke="#aeb9c7" stroke-width="4"/><circle cx="48" cy="74" r="6" fill="#aeb9c7"/><rect x="58" y="71" width="22" height="5" fill="#aeb9c7"/><rect x="38" y="61" width="47" height="3" fill="#aeb9c7"/></svg>

<div class="abs feature-label">LOREM IPSUM DOLOR SIT</div>
<svg class="abs feature-arrow" width="12" height="16" viewBox="0 0 12 16"><polygon points="0,0 12,8 0,16" fill="#0d1b3a"/></svg>
<p class="abs feature-text">Lorem ipsum dolor sit amet, consectetuer adipiscing elit, sed diam nonummy nibh euismod tincidunt ut laoreet</p>

<section class="abs dashboard"></section>
<h2 class="abs section-title dashboard-title" style="top:1166px"><span class="hl">High Profile Support</span> For Distributed<br><span class="hl">Blockchain</span> Technology</h2>
<div class="abs rule" style="top:1239px;background:var(--navy-deep)"></div>
<p class="abs section-sub dashboard-sub" style="top:1258px;color:#e2e6ee">Lorem ipsum dolor sit amet, consectetuer adipiscing elit,</p>
<div class="abs hands-tablet" role="img" aria-label="Photograph of hands holding a tablet showing an account balance dashboard"></div>
<svg class="abs" style="left:606px;top:1370px" width="30" height="30" viewBox="0 0 30 30"><circle cx="15" cy="15" r="14" fill="#e3283a"/><rect x="12" y="7" width="6" height="16" fill="#fff"/><rect x="7" y="12" width="16" height="6" fill="#fff"/></svg>
<p class="abs dashboard-text">Lorem ipsum dolor sit amet, consectetuer adipiscing elit, sed diam nonummy nibh euismod tincidunt ut laoreet dolore magna aliquam erat volutpat.</p>
<div class="abs btn btn-yellow" style="left:650px;top:1448px;width:150px">GET STARTED</div>

<section class="abs security"></section>
<h2 class="abs section-title security-title" style="top:1653px">High Profile <span class="hl">Support For Distributed</span><br>Blockchain <span class="hl">Technology</span></h2>
<div class="abs rule" style="top:1726px"></div>
<p class="abs section-sub" style="top:1745px">Lorem ipsum dolor sit amet, consectetuer adipiscing elit.</p>
<h3 class="abs security-heading">LOREM IPSUM DOLOR SIT AMET</h3>
<p class="abs security-text">Lorem ipsum dolor sit amet, consectetuer adipiscing elit, sed diam nonummy nibh euismod tincidunt ut laoreet dolore magna aliquam erat volutpat. Ut wisi enim ad minim veniam, quis nostrud exerci tation ullamcorper.</p>
<div class="abs btn btn-yellow" style="left:312px;top:1973px;width:151px">GET STARTED</div>
<div class="abs btn btn-slate" style="left:477px;top:1973px;width:151px">GET STARTED</div>
<div class="abs padlock" role="img" aria-label="Illustration of a steel and dark blue padlock"></div>

<section class="abs locations" role="img" aria-label="Faded street map of a city district"></section>
<h2 class="abs section-title locations-title" style="top:2127px">High Profile <span class="hl">Support For Distributed</span><br>Blockchain <span class="hl">Technology</span></h2>
<div class="abs rule" style="top:2200px"></div>
<p class="abs section-sub" style="top:2219px">Lorem ipsum dolor sit amet, consectetuer adipiscing elit.</p>
<div class="abs envelope" role="img" aria-label="Illustration of an open red envelope holding a letter"></div>

<div class="abs contact">
  <div class="row browse">Browse Locations</div>
  <div class="row"><span class="tag">Headquarters</span></div>
  <div class="row">Harborline Offices</div>
  <div class="row">12 Keel Street</div>
  <div class="row">Portsmouth, NH 03801</div>
  <div class="row">USA</div>
</div>
<div class="abs contact contact-col2">
  <div class="row"><span class="tag">United States</span></div>
  <div class="row">+1 555 014 2200</div>
  <div class="row"><span class="tag">Canada</span></div>
  <div class="row">+1 555 017 3300</div>
  <div class="row"><span class="tag">United Kingdom</span></div>
  <div class="row">+44 20 7946 0123</div>
</div>
<div class="abs btn btn-yellow" style="left:580px;top:2459px;width:151px">GET STARTED</div>

</body>
</html>
```